Website design

we need to build up a web site for our newly established personal business (selling ladies accessories customized specifically for each buyer)
Currently we are on Instagram only but it is becoming more and more important to have a website go to our account at instagram to know more about the business: velrino87

Regarding number of pages, please find them below but they might be
extended as the site gets bigger

- Email account ( 2 pages )
- Whats up icon ( 1 page )
- search icon ( 1 page it will be the result )
- Customer feed back ( 1 page with pictures )
- shipping icon ( 1 page )
- bank account details ( 1 page )
- Links ( Home - Hand made accessories - Gold Plated - Silver - Gift )
- Hand made Accessories ( many pages * more than 200 pages )
- Gold plated ( the same idea of the handmade accessories )
- Silver ( ( the same idea of the handmade accessories )
- Git ( the same idea of the handmade accessories )
- Cart page ( 1 page )
- latest picture ( Flash picture )
- Today's deals ( 1 page )
- Live chat area ( chat )
- sign your email area ( 1 page )

Target Market(s)

1- Ladies
2- Teenager girls
3- Male welling to gift female

Requirements
Must have
• 1- It must have an easy way to add more pictures on new products with their model numbers
2- It must have a shopping process from viewing the products, selecting / deselecting multiple products till check out and payment methode (either by credit card or by directly depositing in out account)
3- showing the seperate and accumalating prices as customers buying more products
4- feedback on each product
5- Clear icons at the front page for new products (changed periodically)
6- Ability to search
7- Showing prodcuts categories (like tradora and kelvaro)
8- a process to design the accossory by the buyer (selection field, dropdown list in each stage) example: select your "wrist size" (followed by dropdown list showing size in cm) then select "beads color" (followed by dropdown list showing available colors) seclect number of beads followed by dropdown list showing numbers etc.
9- it must be simple to avoide complications while shopping
10- It must accept Arabic language as many customers are arabic speakers
Nice to have

• 1- Reflects the ladies/femenen taste
2- New products icons should be shown at the main page and gets in and out in a smoothy way (not fast and rapid)
3- Modern feeling
4- it is better to have images while customer going through customizing the products to their need (eg. showing a hand wrist surronded by a measure while asking the customer to give the hand wrist size, etc.)

```html
<!DOCTYPE html>
<html lang="en">
<head>
<meta charset="utf-8">
<title>Velrino87 – About Us</title>
<link rel="stylesheet" href="https://fonts.googleapis.com/css2?family=Oswald:wght@400;500;600&family=Open+Sans:wght@400&display=swap">
<style>
  :root {
    --bg-page: #e9e9e9;
    --charcoal: #464646;
    --charcoal-light: #555555;
    --charcoal-dark: #3a3a3a;
    --topbar: #2a2a2a;
    --teal: #1ba7b3;
    --teal-panel: #174a4c;
    --teal-panel-light: #1e5a5c;
    --nav-fill: #4d4d4d;
    --nav-ring: #2c2c2c;
    --text-light: #f2f2f2;
    --text-body: #e6e6e6;
  }
  * { margin: 0; padding: 0; box-sizing: border-box; }
  html, body { width: 1200px; height: 782px; overflow: hidden; background: var(--bg-page); }
  .site {
    position: relative; width: 1200px; height: 782px; overflow: hidden;
    background: var(--charcoal);
    font-family: "Open Sans", Arial, sans-serif;
  }
  .backdrop { position: absolute; inset: 0; }
  .topbar {
    position: absolute; left: 0; top: 0; width: 100%; height: 20px;
    background: var(--topbar);
  }
  .topbar-dots { position: absolute; right: 14px; top: 4px; display: flex; gap: 6px; }
  .topbar-dots span {
    width: 12px; height: 12px; border-radius: 50%;
    border: 1px solid #9a9a9a; background: #3a3a3a;
  }
  .nav-line {
    position: absolute; left: 372px; top: 20px; width: 5px; height: 762px;
    background: var(--teal);
  }
  .nav-item {
    position: absolute; border-radius: 50%;
    background: var(--nav-fill);
    border: 5px solid var(--nav-ring);
    box-shadow: 0 3px 8px rgba(0,0,0,.45);
    display: flex; align-items: center; justify-content: center;
    font-family: "Oswald", "Arial Narrow", sans-serif; font-weight: 500;
    color: var(--text-light); font-size: 15px; text-transform: uppercase;
    text-decoration: none;
  }
  .nav-item--small { width: 90px; height: 90px; }
  .nav-item--active { border-color: var(--teal); }
  .nav-item--brand { width: 150px; height: 150px; font-size: 28px; font-weight: 600; letter-spacing: .5px; }
  .about {
    position: absolute; left: 940px; top: 306px; width: 220px;
  }
  .about-title {
    display: inline-block;
    font-family: "Oswald", "Arial Narrow", sans-serif; font-weight: 600;
    font-size: 46px; line-height: 1; color: var(--text-light);
    border-left: 4px solid var(--teal); border-right: 4px solid var(--teal);
    padding: 0 6px;
  }
  .about-text {
    margin-top: 6px; font-size: 14px; line-height: 28px; color: var(--text-body);
  }
</style>
</head>
<body>
<main class="site">
  <svg class="backdrop" width="1200" height="782" viewBox="0 0 1200 782" role="img" aria-label="Charcoal background with a faint floral damask pattern">
    <rect width="1200" height="782" fill="var(--charcoal)"/>
    <polygon points="470,20 1200,20 1200,64 1142,64 458,328" fill="var(--charcoal-light)"/>
    <polygon points="0,20 470,20 458,328 579,782 0,782" fill="var(--charcoal-dark)" opacity=".35"/>
    <polygon class="teal-panel" points="458,328 1142,64 1200,64 1200,646 579,719" fill="var(--teal-panel)"/>
    <polygon points="458,328 1142,64 1200,64 1200,120 700,330" fill="var(--teal-panel-light)" opacity=".8"/>
  </svg>

  <header class="topbar">
    <div class="topbar-dots"><span></span><span></span><span></span><span></span></div>
  </header>

  <nav class="main-nav">
    <div class="nav-line"></div>
    <a class="nav-item nav-item--small" style="left:330px; top:178px;">Collection</a>
    <a class="nav-item nav-item--small nav-item--active" style="left:330px; top:298px;">About Us</a>
    <a class="nav-item nav-item--brand" style="left:300px; top:428px;">Velrino87</a>
    <a class="nav-item nav-item--small" style="left:330px; top:618px;">Designs</a>
  </nav>

  <section class="about">
    <h1 class="about-title">About Us</h1>
    <p class="about-text">Lorem ipsum dolor sit amet, nam ex sint dolore accommodare, his summo viris placerat ei. Sed ei detraxit elaboraret dissentias, at eam quando expetenda. In docendi indoctum sit, nec ut graecis lobortis. His justo nostrum ut. Malis comprehensam eu vix, eu causae adipisci mentitum mea, an usu decore iriure postulant.</p>
  </section>
</main>
</body>
</html>
```